Quarrel Ridge Advisory Business Card

Quarrel Ridge Advisory is a company that provides consulting services to the Mining Industry.

Whilst Quarrel Ridge Advisory is an Australian based company its client base is the global mining industry.

The essence of Quarrel Ridge Advisory is its a can do organisation that can make a difference to its clients by providing quality assistance and form lasting relationships.
Updates

Target Market(s)

The global Mining Industry.

Industry/Entity Type

Mining

Font styles to use
Serif

Colors

Designer to choose colors to be used in the design.

Requirements
Nice to have
• My thinking is the card would look good in black given the logo.

I would like to see written on the back side of the card " Providing Metallurgical, Management and Corporate Services to the Mining Industry"

```html
<!DOCTYPE html>
<html lang="en">
<head>
<meta charset="utf-8">
<title>Quarrel Ridge Advisory – Business Card</title>
<link href="https://fonts.googleapis.com/css2?family=Tinos:wght@400;700&display=swap" rel="stylesheet">
<style>
  :root {
    --stage: #d9d8d6;
    --card: #050505;
    --gold: #f2b131;
    --ink: #ffffff;
    --rule: #e6e6e6;
  }
  * { margin: 0; padding: 0; box-sizing: border-box; }
  html, body { width: 1200px; height: 864px; overflow: hidden; }
  body {
    background: var(--stage);
    font-family: "Tinos", "Times New Roman", serif;
    position: relative;
  }
  .card {
    position: absolute;
    width: 560px;
    height: 320px;
    background: var(--card);
    color: var(--ink);
  }
  .card--back { left: 580px; top: 90px; }
  .card--front { left: 60px; top: 460px; }

  .brand-name {
    font-family: "Tinos", "Times New Roman", serif;
    font-weight: 700;
    color: var(--gold);
    text-transform: uppercase;
    line-height: 1.05;
    letter-spacing: 0.02em;
  }

  /* back side */
  .card--back .brand-name {
    position: absolute;
    left: 0; right: 0; top: 96px;
    text-align: center;
    font-size: 40px;
  }
  .card--back .tagline {
    position: absolute;
    left: 0; right: 0; top: 214px;
    text-align: center;
    font-size: 17px;
  }

  /* front side */
  .card--front .brand-name {
    position: absolute;
    left: 40px; top: 112px;
    width: 210px;
    font-size: 33px;
  }
  .divider {
    position: absolute;
    left: 275px; top: 50px;
    width: 2px; height: 220px;
    background: var(--rule);
  }
  .contact {
    position: absolute;
    left: 300px; top: 56px;
    width: 240px;
  }
  .person-name {
    font-size: 22px;
    letter-spacing: 0.04em;
    text-transform: uppercase;
    padding-left: 26px;
  }
  .person-role {
    font-size: 12px;
    padding-left: 26px;
    margin-bottom: 18px;
  }
  .contact-list { list-style: none; }
  .contact-item {
    display: flex;
    align-items: flex-start;
    gap: 10px;
    font-size: 16px;
    line-height: 1.2;
    margin-bottom: 8px;
  }
  .contact-icon { flex: 0 0 16px; width: 16px; height: 16px; margin-top: 1px; fill: var(--gold); }
</style>
</head>
<body>

<section class="card card--back" aria-label="Business card back">
  <p class="brand-name">Quarrel Ridge<br>Advisory</p>
  <p class="tagline">We provide consulting services to the Mining Industry..</p>
</section>

<section class="card card--front" aria-label="Business card front">
  <p class="brand-name">Quarrel Ridge Advisory</p>
  <div class="divider"></div>
  <div class="contact">
    <p class="person-name">Marcus Hale</p>
    <p class="person-role">Managing Director</p>
    <ul class="contact-list">
      <li class="contact-item">
        <svg class="contact-icon" viewBox="0 0 16 16" aria-hidden="true"><path d="M2 6c0-2 2-3 6-3s6 1 6 3v1h-3V5.5H5V7H2z"/><path d="M4 8h8l1.5 5h-11z"/></svg>
        <span>0098 7654 321</span>
      </li>
      <li class="contact-item">
        <svg class="contact-icon" viewBox="0 0 16 16" aria-hidden="true"><path d="M1 3h14v10H1z M2.5 4.5 8 9l5.5-4.5" fill="none" stroke="#f2b131" stroke-width="1.5"/><path d="M1 3h14L8 8.5z"/></svg>
        <span>info@quarrelridge.com</span>
      </li>
      <li class="contact-item">
        <svg class="contact-icon" viewBox="0 0 16 16" aria-hidden="true"><path d="M1 2h14v9H1zm1.5 1.5v6h11v-6z"/><path d="M6 12h4v1.5h2V15H4v-1.5h2z"/></svg>
        <span>www.quarrelridge.com</span>
      </li>
      <li class="contact-item">
        <svg class="contact-icon" viewBox="0 0 16 16" aria-hidden="true"><path d="M8 1 0.5 8H3v7h4v-4h2v4h4V8h2.5z"/></svg>
        <span>Harlow Consulting Inc 000<br>Ave Carden, NJ 00000</span>
      </li>
    </ul>
  </div>
</section>

</body>
</html>
```